Verpackungen für neue online Schokoladenmarke
Zielgruppe
Eine neue online Schokoladenmarke deren Zielgruppe sind anspruchsvolle Schokoladenliebhaber,
denn die Schokolade wird aus Kakaobohnen langzeitgewalzt.
Die Käufer essen nicht süß, sondern wünschen den wirklichen Kakaobohnengeschmack ohne
Zusatzstoffe.
Die Schokolade wird nur online verkauft.
Aufgabenstellung
Markenname: nib4tab Chocolate ---------- oder----- NIB4TAB Chocolate oder ?
Der Markenname soll dominant sein, und die Vorderseite eines Tafelkartons prägen, als
Umverpackung 80 x 160 mm - die Vorderseite, nur die ist hier beauftragt.
Obwohl Bio, muss die Verpackung nicht recycelt oder 'alternativ' aussehen, nicht im Öko - Design auftreten.
Bitte keine angebissenen Schokotafeln, Sahnetöpfe oder sonstige altmodischen Grafiken nutzen.
Der Firmenname nib4tab soll (gut lesbar) gestaltet werden, in Groß- oder Kleinbuchstaben etc. Eventuell
einen Bezug auf Online haben, oder auch nicht...
Der Gewinner kann ggf. weitere Designaufträge und auch die Layouts bzw. Datenübergabe für den
Kartonhersteller machen. Dauerbetreuung erwünscht..!

```html
<!DOCTYPE html>
<html lang="en">
<head>
<meta charset="utf-8">
<title>nib4tab Chocolate – front panel</title>
<link rel="stylesheet" href="https://fonts.googleapis.com/css2?family=Quicksand:wght@300;400&display=swap">
<style>
  :root {
    --ink-dark: #1d1d1f;
    --ornament-tone: #3a3122;
    --cocoa-red: #990404;
    --gold: #e9b420;
    --gold-light: #f6d56a;
    --gold-deep: #c8921a;
  }
  * { margin: 0; padding: 0; box-sizing: border-box; }
  html, body {
    width: 1200px;
    height: 2400px;
    overflow: hidden;
    background: var(--ink-dark);
  }
  .panel {
    position: relative;
    width: 1200px;
    height: 2400px;
    overflow: hidden;
    background: var(--cocoa-red);
    font-family: "Quicksand", sans-serif;
  }
  .panel-shapes {
    position: absolute;
    inset: 0;
  }
  .brand-frame {
    position: absolute;
    left: 184px;
    top: -4px;
    width: 868px;
    height: 630px;
    border: 3px solid var(--gold);
    background: var(--ink-dark);
    display: flex;
    align-items: center;
    justify-content: center;
  }
  .brand-name {
    font-family: "Quicksand", sans-serif;
    font-weight: 400;
    font-size: 190px;
    letter-spacing: 4px;
    color: var(--gold);
    line-height: 1;
  }
  .product-name {
    position: absolute;
    left: 0;
    width: 1200px;
    top: 1600px;
    text-align: center;
    font-weight: 300;
    font-size: 182px;
    letter-spacing: 10px;
    color: var(--gold);
    line-height: 1;
  }
  .net-weight {
    position: absolute;
    left: 79px;
    top: 2288px;
    font-weight: 300;
    font-size: 64px;
    color: var(--gold);
    line-height: 1;
  }
  .seal-square {
    position: absolute;
    left: 479px;
    top: 2123px;
    width: 269px;
    height: 300px;
    border: 3px solid var(--gold-deep);
    background: var(--ink-dark);
  }
</style>
</head>
<body>
  <main class="panel">
    <svg class="panel-shapes" width="1200" height="2400" viewBox="0 0 1200 2400" aria-hidden="false">
      <defs>
        <linearGradient id="ornamentFill" x1="0" y1="0" x2="1" y2="1">
          <stop offset="0" stop-color="#2a261f"/>
          <stop offset="0.5" stop-color="var(--ornament-tone)"/>
          <stop offset="1" stop-color="#2a261f"/>
        </linearGradient>
        <linearGradient id="goldEdge" x1="0" y1="0" x2="1" y2="0">
          <stop offset="0" stop-color="#d6a21c"/>
          <stop offset="0.55" stop-color="#fbe7a0"/>
          <stop offset="1" stop-color="#d6a21c"/>
        </linearGradient>
      </defs>
      <polygon class="ornament-field" points="0,0 1200,0 1200,838 603,1448 0,838"
               fill="url(#ornamentFill)" role="img"
               aria-label="Fine gold line ornament of swirls, paisley and beaded arcs on dark ground"/>
      <polyline class="chevron-edge" points="0,838 603,1441 1200,844"
                fill="none" stroke="url(#goldEdge)" stroke-width="12"/>
    </svg>

    <div class="brand-frame">
      <span class="brand-name">nib4tab</span>
    </div>

    <p class="product-name">choclate</p>
    <p class="net-weight">100g</p>
    <div class="seal-square"></div>
  </main>
</body>
</html>
```